Create and Design Brand Guidelines for IT Company

Brindle Networks Logo and Branding Objective
Brindle Networks is upgrading its brand assets, marketing collateral and website. The company is seeking a graphic designer's expertise to develop a style guide that creates brand consistency and communicates to internal and external stakeholders how to position the Brindle Networks brand when assigned tasks relating to the brand. The brand style guide should have information about the logo and clear usage guidelines, a recommended font to use, a colour profile including HEX code, RGB, CMYK, Pantone codes, and iconography recommendations. Details about the company tone, voice and photography usage will be added by Brindle Networks.
Look and feel
Each slider illustrates characteristics of the customer's brand and the style your logo design should communicate.

```html
<!DOCTYPE html>
<html lang="en">
<head>
<meta charset="UTF-8">
<title>Brindle Networks Brand Guidelines — Typography &amp; Implementations</title>
<link href="https://fonts.googleapis.com/css2?family=Inter:wght@300;400;500;600;700&display=swap" rel="stylesheet">
<style>
  :root {
    --brand-green: #8fcd4f;
    --ink: #111111;
    --ink-soft: #2a2a2a;
    --paper: #ffffff;
    --photo-dark: #5b5d5f;
    --photo-mid: #a6a6a6;
    --photo-light: #ececec;
  }
  * { margin: 0; padding: 0; box-sizing: border-box; }
  html, body { width: 1200px; height: 848px; overflow: hidden; background: var(--paper); }
  body { font-family: "Inter", sans-serif; color: var(--ink); position: relative; }

  .spread { position: relative; width: 1200px; height: 848px; }
  .page-title { position: absolute; top: 94px; font-size: 36px; font-weight: 700; letter-spacing: -0.3px; line-height: 1.2; }
  .title-rule { position: absolute; top: 146px; height: 3px; background: var(--brand-green); }

  .typeface-intro { position: absolute; left: 61px; top: 170px; width: 461px; font-size: 11px; font-weight: 300; line-height: 15.5px; text-align: justify; }

  .specimen-bar { position: absolute; left: 63px; top: 275px; width: 7px; height: 344px; background: var(--brand-green); }
  .specimen { position: absolute; left: 89px; }
  .specimen-heading { top: 274px; width: 360px; font-size: 20px; font-weight: 600; line-height: 25px; }
  .specimen-sub1 { top: 364px; width: 360px; font-size: 17px; font-weight: 500; line-height: 22px; }
  .specimen-sub2 { top: 428px; width: 360px; font-size: 13.5px; font-weight: 400; line-height: 17.5px; }
  .specimen-body { top: 483px; width: 352px; font-size: 13.5px; font-weight: 300; line-height: 17px; text-align: justify; }

  .marker { position: absolute; left: 477px; width: 24px; height: 24px; border: 1px solid var(--ink); border-radius: 50%; font-size: 12px; font-weight: 300; display: flex; align-items: center; justify-content: center; }

  .type-legend { position: absolute; left: 61px; top: 665px; list-style: none; font-size: 11.5px; }
  .type-legend li { height: 21px; display: flex; align-items: center; font-weight: 300; }
  .legend-num { width: 13px; height: 13px; border: 1px solid var(--ink); border-radius: 50%; font-size: 8.5px; display: inline-flex; align-items: center; justify-content: center; margin-right: 4px; }
  .legend-label { width: 86px; }
  .legend-value { font-weight: 500; }
  .legend-value.semibold { font-weight: 600; }
  .legend-value.regular { font-weight: 400; }
  .legend-value.light { font-weight: 300; }

  .section-label { position: absolute; left: 651px; font-size: 19px; font-weight: 300; color: var(--ink-soft); }
  .mockup { position: absolute; }
  .mockup-card { left: 653px; top: 229px; width: 253px; height: 181px; background: linear-gradient(135deg, var(--photo-dark) 0%, #7a7c7e 45%, var(--brand-green) 100%); }
  .mockup-letterhead { left: 651px; top: 502px; width: 206px; height: 206px; background: var(--photo-mid); }
  .mockup-envelope { left: 857px; top: 502px; width: 261px; height: 148px; background: var(--photo-light); }

  .footer-band { position: absolute; left: 0; top: 795px; width: 1200px; height: 28px; background: var(--brand-green); font-size: 10px; font-weight: 400; }
  .folio { position: absolute; top: 0; height: 28px; display: flex; align-items: center; }
  .folio-left { left: 12px; }
  .folio-right { right: 16px; }
  .folio-divider { width: 1px; height: 20px; background: var(--ink); margin: 0 15px; }
</style>
</head>
<body>
<main class="spread">

  <section class="page page-typography">
    <h1 class="page-title" style="left:55px;">Typography</h1>
    <div class="title-rule" style="left:55px; width:467px;"></div>

    <p class="typeface-intro">The typeface of our brand is Inter. Inter is a sans-serif font that reflects modernism and simplicity in its form. Inter is also available is multiple weights and has excellent legibility, so it can be applied even in the smallest media, such as mobile app.</p>

    <div class="specimen-bar"></div>
    <p class="specimen specimen-heading">Brindle Networks Ltd is a premium Cloud-first IT company offering various MSP solutions</p>
    <p class="specimen specimen-sub1">Lorem ipsum dolor sit amet, consectetur adipiscing elit.</p>
    <p class="specimen specimen-sub2">sed do eiusmod tempor incididunt ut labore et dolore magna aliqua. Ut enim ad minim veniam</p>
    <p class="specimen specimen-body">Sed ut perspiciatis unde omnis iste natus error sit voluptatem accusantium doloremque laudantium, totam rem aperiam, eaque ipsa quae ab illo inventore veritatis et quasi architecto beatae vitae dicta sunt explicabo. Nemo enim ipsam voluptatem quia voluptas sit aspernatur aut odit aut fugit, sed quia consequuntur magni dolores eos qui ratione voluptatem sequi nesciunt.</p>

    <span class="marker" style="top:294px;">1</span>
    <span class="marker" style="top:372px;">2</span>
    <span class="marker" style="top:437px;">3</span>
    <span class="marker" style="top:536px;">4</span>

    <ul class="type-legend">
      <li><span class="legend-num">1</span><span class="legend-label">Heading/title&nbsp;&nbsp;:</span><span class="legend-value semibold">Inter Semi Bold</span></li>
      <li><span class="legend-num">2</span><span class="legend-label">Subheading 1 :</span><span class="legend-value">Inter Medium</span></li>
      <li><span class="legend-num">3</span><span class="legend-label">Subheading 2 :</span><span class="legend-value regular">Inter Regular</span></li>
      <li><span class="legend-num">4</span><span class="legend-label">Body text&nbsp;&nbsp;&nbsp;&nbsp;&nbsp;&nbsp;&nbsp;&nbsp;:</span><span class="legend-value light">Inter Light</span></li>
    </ul>
  </section>

  <section class="page page-implementations">
    <h1 class="page-title" style="left:650px;">Implementations</h1>
    <div class="title-rule" style="left:653px; width:462px;"></div>

    <h2 class="section-label" style="top:184px;">Business card</h2>
    <div class="mockup mockup-card" role="img" aria-label="Business card mockup: stacked grey and green Brindle Networks business cards"></div>

    <h2 class="section-label" style="top:457px;">Letterhead and Envelope</h2>
    <div class="mockup mockup-letterhead" role="img" aria-label="Letterhead mockup: white Brindle Networks letterhead with green footer on grey background"></div>
    <div class="mockup mockup-envelope" role="img" aria-label="Envelope mockup: white Brindle Networks envelope with green base stripe"></div>
  </section>

  <footer class="footer-band">
    <div class="folio folio-left"><span>07</span><span class="folio-divider"></span><span>Brindle Networks Brand Guidelines</span></div>
    <div class="folio folio-right"><span>Brindle Networks Brand Guidelines</span><span class="folio-divider"></span><span>08</span></div>
  </footer>

</main>
</body>
</html>
```